Bramblewick Acres Organic Hemp Company needs an OLD WORLD Label for CBD Bottle!

*UPDATE* Increased the budget! Please keep in mind, we are also open to "modern vintage", "hipster vintage" and other forms of retro emulation. Whatever the case, we are looking for a small work of art, like an indie Gin bottle- not the clinical drab that every other CBD bottle has. Also, don't be afraid to incorporate color, or alter the logo (color wise), we want something breathtaking in a small package. Show us what that looks like to you!

*UPDATE* Please take a moment to visit this link to see the types of branding we are interested in: https://www.pinboardly.example/tobiasquentinharlow/neat-branding/

We are an Organic Hemp company about to launch it's first line of products. This design is for our CBD Bottle. We have a pre-existing logo that we need developed and expanded into a label. Our theme is Old World, Victorian, Vintage, Turn of the Century (there are too many names for this genre, you get it...) We want our brand to convey a sense of intrigue, artisan quality and a bit of mystery. Very different from the clinical look of most CBD tinctures. We are HUGE fans of the design house "Copper and Copper" and would LOVE something that conjures that feel.

The first attachment will be our current logo, and I will be adding "inspiration" as I can.

The second attachment will be a rendition of our raw logo with regulatory information. This is what we need this spiced up! You DO NOT have to follow this design, but the same information needs to be on there. It's very likely that the line work will be in "gold foil".

Any additional attachments are for "inspiration", what we're looking for.

Feel free to explore with it, we are looking for something breathtaking!

Thanks!

Tobias
Bramblewick Acres
Verdant Curios

Target Market(s)

Younger, Hipster Demographic and all who are interested in Organic Products!

Colors

Designer to choose colors to be used in the design.

Requirements
Must have
• Full Spectrum Hemp Extract CDB Oil 1000mg Natural Flavor 1.02 FL OZ (30 ML)
Should not have
• Cannabis, Cannabis leaves, Marijuana etc...

```html
<!DOCTYPE html>
<html lang="en">
<head>
<meta charset="utf-8">
<title>Bramblewick Acres CBD Oil Label</title>
<link href="https://fonts.googleapis.com/css2?family=Rye&family=Montserrat:wght@700;800&family=Alfa+Slab+One&display=swap" rel="stylesheet">
<style>
  :root {
    --backdrop: #efefef;
    --label-black: #0e0e0e;
    --foil-gold: #c9ac3f;
    --foil-gold-light: #dcc660;
    --ink-white: #f4f2ec;
  }
  * { margin: 0; padding: 0; box-sizing: border-box; }
  html, body {
    width: 1200px;
    height: 1050px;
    overflow: hidden;
    background: var(--backdrop);
  }
  .canvas {
    position: relative;
    width: 1200px;
    height: 1050px;
    display: flex;
    align-items: center;
    justify-content: center;
  }
  .label {
    position: relative;
    width: 860px;
    height: 980px;
    background: var(--label-black);
    color: var(--ink-white);
    text-align: center;
  }
  .brand-lockup {
    position: absolute;
    top: 80px;
    left: 0;
    right: 0;
    height: 400px;
  }
  .brand-established {
    position: absolute;
    top: 20px;
    left: 0;
    right: 0;
    font-family: "Montserrat", sans-serif;
    font-weight: 700;
    font-size: 15px;
    letter-spacing: 5px;
    color: var(--ink-white);
  }
  .brand-name {
    position: absolute;
    top: 70px;
    left: 130px;
    width: 520px;
    font-family: "Rye", serif;
    font-size: 92px;
    line-height: 1.02;
    color: var(--ink-white);
    text-align: left;
  }
  .brand-name .line-two {
    display: block;
    padding-left: 120px;
    font-size: 78px;
  }
  .brand-mark {
    position: absolute;
    top: 160px;
    left: 620px;
    width: 150px;
    height: 150px;
    border-radius: 50%;
    border: 3px solid var(--foil-gold);
  }
  .brand-tagline {
    position: absolute;
    top: 330px;
    left: 0;
    right: 0;
    font-family: "Montserrat", sans-serif;
    font-weight: 800;
    font-size: 22px;
    letter-spacing: 7px;
    color: var(--ink-white);
    text-transform: uppercase;
  }
  .product-kind {
    position: absolute;
    top: 508px;
    left: 0;
    right: 0;
    font-family: "Rye", serif;
    font-size: 34px;
    color: var(--foil-gold);
    letter-spacing: 1px;
  }
  .product-name {
    position: absolute;
    top: 540px;
    left: 0;
    right: 0;
    font-family: "Rye", serif;
    font-size: 150px;
    line-height: 1;
    color: var(--foil-gold);
    letter-spacing: 4px;
  }
  .divider {
    position: absolute;
    top: 700px;
    left: 175px;
    width: 510px;
    height: 40px;
  }
  .strength {
    position: absolute;
    top: 748px;
    left: 0;
    right: 0;
    font-family: "Alfa Slab One", serif;
    font-size: 64px;
    line-height: 1;
    color: var(--ink-white);
  }
  .flavor {
    position: absolute;
    top: 828px;
    left: 0;
    right: 0;
    display: flex;
    justify-content: center;
    align-items: center;
    gap: 14px;
  }
  .flavor-rule { width: 54px; height: 2px; background: var(--foil-gold); }
  .flavor-text {
    font-family: "Rye", serif;
    font-size: 30px;
    color: var(--foil-gold);
    border-left: 2px solid var(--foil-gold);
    border-right: 2px solid var(--foil-gold);
    padding: 2px 16px;
    line-height: 1.1;
  }
  .volume {
    position: absolute;
    top: 898px;
    left: 0;
    right: 0;
    font-family: "Rye", serif;
    font-size: 26px;
    color: var(--ink-white);
  }
</style>
</head>
<body>
  <main class="canvas">
    <section class="label">
      <header class="brand-lockup">
        <p class="brand-established">ORGANIC ARTISANAL HEMP · ESTD 2019</p>
        <h1 class="brand-name">Bramblewick<span class="line-two">Acres</span></h1>
        <div class="brand-mark"></div>
        <p class="brand-tagline">Verdant Curios</p>
      </header>

      <p class="product-kind">Full Spectrum Hemp Extract</p>
      <h2 class="product-name">CBD OIL</h2>

      <svg class="divider" viewBox="0 0 510 40" aria-hidden="true">
        <line x1="0" y1="8" x2="510" y2="8" stroke="var(--foil-gold)" stroke-width="4"/>
        <line x1="30" y1="18" x2="480" y2="18" stroke="var(--foil-gold)" stroke-width="1.5"/>
      </svg>

      <p class="strength">1000 MG</p>

      <div class="flavor">
        <span class="flavor-rule"></span>
        <span class="flavor-text">Natural Flavor</span>
        <span class="flavor-rule"></span>
      </div>

      <p class="volume">1.02 FL OZ (30 ML)</p>
    </section>
  </main>
</body>
</html>
```